Business Intelligence/Analytics Technology Company Business Card

We are a higher-end enterprise software development company working with Retailer POS data to provide business intelligence and analytical services to fortune 500 companies.

I have an immediate need for a professional/thick/bold business card. The same design aspects will spiral into more media such as flyers/folders/etc...

Our website is www.brenvolq.com for our product.

I like "Clean" designs if that makes sense, not a lot of "stuff".

The uploaded files, the A logo with the box is the style we're leaning towards, but the A logo without the blue box is all good too... get creative.

Target Market(s)

Executives of large companies, down to VP level..

Industry/Entity Type

Software

Requirements
Must have
• I'm wanting a thick designer like business card.

I think we're going to change our logo to a more quillmesh 8 looking style... http://www.brenvolq.com/card.ai as an example of our current business card.

The winner will also have knowledge of where i can get these things printed.
Nice to have
• Blue-ish color scheme? I'm open to anything. Our Competition is Red, and another is Green. So we'll stick with the Blue.

```html
<!DOCTYPE html>
<html lang="en">
<head>
<meta charset="utf-8">
<title>Brenvolq Business Card</title>
<link rel="stylesheet" href="https://fonts.googleapis.com/css2?family=Source+Sans+3:wght@400;600&display=swap">
<style>
  :root {
    --bg-center: #1e75ad;
    --bg-edge: #2fa6ea;
    --ink-dark: #1f2a33;
    --band-top: #171b1d;
    --band-bottom: #4a5658;
    --band-text: #e4e8ea;
    --mark: #1a2630;
  }
  html, body {
    margin: 0;
    padding: 0;
    width: 1200px;
    height: 720px;
    overflow: hidden;
  }
  .card {
    position: relative;
    width: 1200px;
    height: 720px;
    background: radial-gradient(ellipse 62% 62% at 50% 48%, var(--bg-center) 0%, #2388c6 55%, var(--bg-edge) 100%);
    font-family: "Source Sans 3", "Myriad Pro", Arial, sans-serif;
    overflow: hidden;
  }
  .brand {
    position: absolute;
    left: 34px;
    top: 36px;
    display: flex;
    align-items: center;
    gap: 22px;
  }
  .brand-square {
    width: 92px;
    height: 92px;
    background: var(--mark);
  }
  .brand-name {
    font-size: 76px;
    font-weight: 600;
    letter-spacing: 10px;
    color: var(--mark);
    line-height: 1;
  }
  .person {
    position: absolute;
    right: 146px;
    top: 196px;
    text-align: right;
    color: var(--ink-dark);
  }
  .person-name {
    font-size: 76px;
    font-weight: 400;
    line-height: 1;
    margin: 0;
  }
  .person-title {
    font-size: 38px;
    font-weight: 400;
    line-height: 1;
    margin: 14px 0 0;
  }
  .info-band {
    position: absolute;
    left: 0;
    top: 513px;
    width: 1097px;
    height: 101px;
    background: linear-gradient(to bottom, var(--band-top), var(--band-bottom));
  }
  .info-tab {
    position: absolute;
    left: 1118px;
    top: 513px;
    width: 82px;
    height: 101px;
    background: linear-gradient(to bottom, var(--band-top), var(--band-bottom));
  }
  .address {
    position: absolute;
    left: 40px;
    top: 10px;
    margin: 0;
    font-style: normal;
    color: var(--band-text);
    font-size: 18.5px;
    line-height: 28.5px;
  }
  .contact {
    position: absolute;
    left: 884px;
    top: 38px;
    margin: 0;
    color: var(--band-text);
    font-size: 18.5px;
    line-height: 28px;
    text-align: right;
  }
</style>
</head>
<body>
  <div class="card">
    <div class="brand">
      <div class="brand-square"></div>
      <div class="brand-name">BRENVOLQ</div>
    </div>

    <div class="person">
      <p class="person-name">First Last</p>
      <p class="person-title">President</p>
    </div>

    <div class="info-band">
      <address class="address">
        BRENVOLQ Technology Group, Inc<br>
        Adress<br>
        City State Zip
      </address>
      <p class="contact">
        P: 555 555 555<br>
        F: 555 555 555
      </p>
    </div>
    <div class="info-tab"></div>
  </div>
</body>
</html>
```